Redesign Website

I currently have a website www.quillbrookrehab.com that I would like to have redesigned for esthetics and design limitations with the present platform. I will provide my logo, background logo (attached) , current site, foundation grip PSD.zip (attached) and a questionnaire (attached) from a web design company to provide the input to have an impressive site that pleases the eyes and makes an impact. I would also like the site to be mobile friendly.

IMPORTANT:
- The final PSD must include:
o Homepage Mockup
o Internal Pages Mockup
o Mobile site mockup
o Fonts files used in mockup

Final website will be responsive, using the Foundation Framework. Attached you will find a PSD of the Foundation grid – please use this and include with your final PSD. Here is a link for reference:
http://plenvix.com/article/1053/foundation-s-grid-and-photoshop-what-you-

Target Market(s)

Patients for physical therapy

Industry/Entity Type

It Company

Requirements
Must have
• Pages included in the present site. Photos and design should change.
Nice to have
• Should provide information necessary for patients to schedule an appointment
Should not have
• Should not be difficult to read.

```html
<!DOCTYPE html>
<html lang="en">
<head>
<meta charset="utf-8">
<title>Quillbrook Sports &amp; Orthopedic Physical Therapy</title>
<link rel="stylesheet" href="https://fonts.googleapis.com/css2?family=Arimo:wght@400;700&family=Open+Sans:wght@400;700&display=swap">
<style>
:root{
  --orange:#e8761f;
  --orange-light:#ee8f2c;
  --red:#d8232a;
  --ink:#333;
  --body:#555;
  --muted:#777;
  --band:#a6a6a6;
  --page:#f6f6f6;
  --panel:#ececec;
  --footer:#dcdcdc;
  --foot-bar:#c9c9c9;
}
*{box-sizing:border-box;margin:0;padding:0}
html,body{width:886px;height:1200px;overflow:hidden}
body{position:relative;background:var(--page);font-family:"Arimo",Arial,sans-serif;color:var(--ink)}
.abs{position:absolute}

.site-header{left:0;top:0;width:886px;height:80px;background:#fff}
.brand{left:178px;top:14px;display:flex;align-items:center;gap:8px}
.brand-dot{width:22px;height:22px;border-radius:50%;background:var(--red)}
.brand-name{font-weight:700;color:var(--red);font-size:15px;line-height:17px;width:150px}
.call{right:169px;top:17px;font-size:9px;color:var(--muted)}
.call b{font-weight:400;color:var(--orange);font-size:12px;margin-left:3px}
.social-top{right:170px;top:41px;display:flex;gap:3px}
.social-top span{width:18px;height:18px;background:#e6e6e6;display:block}

.main-nav{left:0;top:80px;width:886px;height:29px;background:var(--orange)}
.main-nav ul{list-style:none;position:absolute;left:186px;top:0;height:29px;font-size:8.5px;color:#fff}
.main-nav li{position:absolute;top:10px;white-space:nowrap}

.hero{left:0;top:109px;width:886px;height:254px;background:linear-gradient(100deg,#d9d4cc 0%,#eae6e0 35%,#d8b5a0 60%,#f1efec 100%)}

.feature-band{left:0;top:363px;width:886px;height:117px;background:var(--band)}
.feature{top:346px;width:181px;height:134px;text-align:center;color:#fff;font-size:15px}
.feature.active{background:var(--orange)}
.feature svg{margin-top:38px}
.feature p{margin-top:12px;letter-spacing:.2px}
.feature.muted{color:#555}

.intro-title{left:179px;top:512px;font-size:13.5px;font-weight:400;color:var(--red)}
.portrait{left:179px;top:551px;width:163px;height:130px;background:#ddd;padding:4px}
.portrait div{width:100%;height:100%;background:linear-gradient(180deg,#f4f4f2 0%,#e8e2dc 55%,#9fb4d2 100%)}
.intro-text{left:179px;top:546px;width:340px;font-size:8px;line-height:14.4px;color:var(--body)}
.intro-text .float{float:left;width:172px;height:140px}

.side-head{left:538px;width:179px;height:27px;background:var(--orange-light);color:#fff;font-size:10px;padding:8px 9px}
.side-panel{left:538px;width:179px;background:var(--panel)}
.contact-panel{top:532px;height:194px}
.lede{position:absolute;left:9px;top:10px;width:150px;font-style:italic;font-size:7.2px;line-height:11px;color:var(--muted)}
.field-label{position:absolute;left:9px;font-size:8px;color:var(--ink)}
.field{position:absolute;left:53px;width:110px;height:15px;background:#fff;border:1px solid #e0e0e0}
.send{position:absolute;left:53px;top:166px;width:60px;height:19px;background:var(--orange);color:#fff;font-size:8px;text-align:center;line-height:19px}
.social-panel{top:769px;height:163px}
.social-list{position:absolute;left:9px;top:9px;width:160px;height:146px;background:#fff}
.social-item{position:absolute;left:12px;display:flex;align-items:center;gap:10px;font-family:"Open Sans",Arial,sans-serif}
.social-item i{width:21px;height:21px;border-radius:4px;background:#b7b7b7;display:block}
.social-item b{display:block;font-size:8.3px;color:#333}
.social-item span{display:block;font-size:8px;color:#444;line-height:10px}

.footer{left:0;top:955px;width:886px;height:213px;background:var(--footer);border-top:3px solid var(--orange)}
.foot-h{top:986px;font-size:13px;font-weight:400;color:#222}
.foot-name{left:178px;top:1022px;font-size:11.5px;line-height:18px;color:#222;width:170px}
.foot-list{left:178px;top:1066px;width:174px;font-size:7.2px;color:#333;list-style:none}
.foot-list li{display:flex;align-items:center;gap:6px;height:15px;white-space:nowrap;overflow:hidden}
.foot-list svg{flex:none}
.map{left:358px;top:1024px;width:161px;height:116px;background:linear-gradient(135deg,#e9e6dc,#d8dcd0 60%,#e5e0cf);border:2px solid #eee}
.hours{left:536px;top:1023px;width:181px;background:#d1d1d1;font-size:7.6px;color:#333}
.hours-row{display:flex;height:19.5px;align-items:center;border-bottom:1px solid #e3e3e3;padding-left:9px}
.hours-row span:nth-child(1){width:60px}
.hours-row span:nth-child(2){width:45px}
.hours-row span:nth-child(3){width:26px;color:#666}
.hours-note{height:20px;line-height:20px;padding-left:9px}

.foot-bar{left:0;top:1168px;width:886px;height:32px;background:var(--foot-bar);font-size:7.4px;color:#555}
.foot-bar .copy{position:absolute;left:179px;top:12px}
.foot-bar .links{position:absolute;right:169px;top:13px}
</style>
</head>
<body>

<header class="abs site-header">
  <div class="abs brand">
    <span class="brand-dot"></span>
    <span class="brand-name">Quillbrook<br>Sports &amp; Orthopedic<br>Physical Therapy</span>
  </div>
  <div class="abs call">Call us: <b>610.555.0148</b></div>
  <div class="abs social-top"><span></span><span></span><span></span><span></span></div>
</header>

<nav class="abs main-nav">
  <ul>
    <li style="left:0">HOME</li>
    <li style="left:62px">ABOUT US</li>
    <li style="left:140px">LOCATION</li>
    <li style="left:200px">HOURS</li>
    <li style="left:260px">SERVICES</li>
    <li style="left:320px">NEW PATIENTS</li>
    <li style="left:400px">TESTIMONIAL</li>
    <li style="left:480px">CONTACT US</li>
  </ul>
</nav>

<div class="abs hero" role="img" aria-label="Therapist treating a patient's shoulder on a treatment table"></div>

<div class="abs feature-band"></div>
<div class="abs feature active" style="left:177px">
  <svg width="40" height="44" viewBox="0 0 40 44"><path d="M30 3 C16 8 8 20 10 34 L14 30 C14 20 20 12 30 3Z" fill="#fff"/><path d="M6 40 C12 36 18 42 24 38 S32 38 36 40" stroke="#fff" stroke-width="2" fill="none"/></svg>
  <p>OUR STORY</p>
</div>
<div class="abs feature muted" style="left:358px">
  <svg width="44" height="44" viewBox="0 0 44 44"><circle cx="22" cy="22" r="14" fill="none" stroke="#eee" stroke-width="7" stroke-dasharray="5 3.8"/><circle cx="22" cy="22" r="10" fill="#eee"/><circle cx="22" cy="22" r="5" fill="#a6a6a6"/></svg>
  <p>OUR SERVICE</p>
</div>
<div class="abs feature muted" style="left:536px">
  <svg width="48" height="44" viewBox="0 0 48 44"><path d="M24 2 L34 6 V16 C34 22 29 26 24 28 C19 26 14 22 14 16 V6Z" fill="#eee"/><path d="M4 34 H16 C20 34 24 36 28 36 H40 V42 H4Z" fill="#eee"/></svg>
  <p>OUR SERVICE</p>
</div>

<h1 class="abs intro-title">Quillbrook Sports &amp; Orthopedic Physical Therapy</h1>
<div class="abs portrait"><div role="img" aria-label="Portrait of the lead physical therapist"></div></div>
<p class="abs intro-text"><span class="float"></span>Our services are the culmination of 15 years experience of Dr. Marcus Hollen, PT, DPT, MS the sports and orthopedic physical therapy arena. Marcus directed the rehabilitation service for the largest orthopedic group in Chester County. He has provided the services for an orthopedic and sports medicine group that specialists in spine, shoulder, elbow, wrist, hand, hip, knee, ankle and foot surgery and treatment. His expertise is the treatment of any and all sports and orthopedic injuries, whether they are the result of trauma, repetitive movements or postures or the result of a surgical intervention. Marcus Hollen, PT, DPT, MS is confident that his extensive knowledge base and manual skills will drive Quillbrook Sports &amp; Orthopedic Physical Therapy to become a keystone in the private practice physical therapy community. Marcus relishes the fact that he is able to provide an atmosphere and facilities that are conducive towards a collective rehabilitation experience for clients that range from adolescents to geriatrics. Come in or correspond with our office. You will see that we value you as a client and would like to make you part of our community! If you have any questions about your injury and the treatment that you would receive, please contact us and you will be comforted in the fact that you have a partner in the community that you can trust.</p>

<div class="abs side-head" style="top:505px">Contact form</div>
<div class="abs side-panel contact-panel">
  <p class="lede">Lorem ipsum dolor sit amet, consectetuer adipiscing elit, sed diam nonummy nibh euismod tincidunt ut laoreet dolore magna aliquam erat volutpat.</p>
  <span class="field-label" style="top:68px">Name</span><span class="field" style="top:65px"></span>
  <span class="field-label" style="top:88px">Email</span><span class="field" style="top:85px"></span>
  <span class="field-label" style="top:108px">Message</span><span class="field" style="top:107px;height:48px"></span>
  <span class="send">SEND FORM</span>
</div>

<div class="abs side-head" style="top:742px">Get Social With Us</div>
<div class="abs side-panel social-panel">
  <div class="social-list">
    <div class="social-item" style="top:14px"><i></i><div><b>150 Likes</b><span>Like us on our page</span></div></div>
    <div class="social-item" style="top:45px"><i></i><div><b>215 Followers</b><span>Follow our updates</span></div></div>
    <div class="social-item" style="top:77px"><i></i><div><b>75 Subscribers</b><span>Watch our videos</span></div></div>
    <div class="social-item" style="top:108px"><i></i><div><b>17 Readers</b><span>Read our news feed</span></div></div>
  </div>
</div>

<footer class="abs footer"></footer>
<h2 class="abs foot-h" style="left:179px">CONTACT US</h2>
<h2 class="abs foot-h" style="left:379px">AREA MAP</h2>
<h2 class="abs foot-h" style="left:537px">OUR HOURS</h2>

<p class="abs foot-name">Quillbrook Sports &amp; Orthopedic Physical Therapy</p>
<ul class="abs foot-list">
  <li><svg width="9" height="10" viewBox="0 0 9 10"><path d="M4.5 0 C2 0 0.5 2 0.5 4 C0.5 6.5 4.5 10 4.5 10 S8.5 6.5 8.5 4 C8.5 2 7 0 4.5 0Z" fill="#e8761f"/><circle cx="4.5" cy="4" r="1.5" fill="#fff"/></svg>218 Ridge Ave Suite 4 Alder Creek, PA 19000</li>
  <li><svg width="9" height="10" viewBox="0 0 9 10"><rect x="0" y="2" width="9" height="6" fill="#e8761f"/><path d="M0 2 L4.5 5.5 L9 2" stroke="#fff" fill="none"/></svg>mhollen@quillbrookrehab.com</li>
  <li><svg width="9" height="10" viewBox="0 0 9 10"><path d="M1 2 H8 V4 H6 V3 H3 V4 H1Z M2 5 H7 V9 H2Z" fill="#e8761f"/></svg>610.555.0148</li>
  <li><svg width="9" height="10" viewBox="0 0 9 10"><rect x="2" y="1" width="5" height="3" fill="#e8761f"/><rect x="0.5" y="4" width="8" height="5" fill="#e8761f"/></svg>610.555.0149 (fax)</li>
  <li><svg width="9" height="10" viewBox="0 0 9 10"><circle cx="4.5" cy="5" r="4" fill="none" stroke="#e8761f"/><path d="M0.5 5 H8.5 M4.5 1 V9" stroke="#e8761f"/></svg>www.quillbrookrehab.com</li>
</ul>

<div class="abs map" role="img" aria-label="Street map of the clinic's neighborhood"></div>

<div class="abs hours">
  <div class="hours-row"><span>Monday</span><span>7:30am</span><span>&#8594;</span><span>8:00pm</span></div>
  <div class="hours-row"><span>Tuesday</span><span>7:30am</span><span>&#8594;</span><span>8:00pm</span></div>
  <div class="hours-row"><span>Wednesday</span><span>7:30am</span><span>&#8594;</span><span>8:00pm</span></div>
  <div class="hours-row"><span>Thursday</span><span>7:30am</span><span>&#8594;</span><span>8:00pm</span></div>
  <div class="hours-row"><span>Friday</span><span>7:30am</span><span>&#8594;</span><span>5:30pm</span></div>
  <div class="hours-note">Saturday by appointment only</div>
</div>

<div class="abs foot-bar">
  <span class="copy">Copyright © 2014. Quillbrook Sports &amp; Orthopedic Physical Therapy</span>
  <span class="links">Print | Sitemap | Login</span>
</div>

</body>
</html>
```